Business Cards Design for the electrical wholesaler: clean bold dynamic :)

We need a business card design that would follow our latest brand guidelines. As an electrical wholesaler we want to bring a fresh look and feel into the industry. The design should be clean bold and dynamic. It should come alive with the renewed energy of our green colour. Our grey colour should keep things balanced and complement the notion of maturity and responsibility. We employ Lato as a corporate font however are not bound by this font and we’re open to interpretation here.

Target Market(s)

Electrical contractors

Industry/Entity Type

Business

Contact Information for Business Card

Logo
Name & Surname: Olena Dovbush
Job Title: Director of Marketing
Email: helen.dovbush@mailvane.example
Cell phone: XXX.XXX.XXXX
Address: 20917 - 87 Ave. Edmonton, AB, Canada. T6K 2R8
Business Phone: 780.555.0187
Website: www.qorvil.example

Font styles to use
Other font styles liked:
• Lato

Requirements
Must have
• Logo & website
Nice to have
• Brand elements - some of them you may find in the attached Brand Guidelines (e.g. three lines on the background signifying "W")

```html
<!DOCTYPE html>
<html lang="en">
<head>
<meta charset="utf-8">
<title>Qorvil Business Cards</title>
<link href="https://fonts.googleapis.com/css2?family=Lato:wght@400;700&display=swap" rel="stylesheet">
<style>
  :root {
    --green: #6aab2e;
    --green-deep: #5c9a26;
    --grey: #3e3f42;
    --grey-dark: #333437;
    --paper: #f3f3f3;
    --ink: #3a3b3e;
    --stage: #1a1a1a;
    --light-text: #e6e6e6;
  }
  * { box-sizing: border-box; margin: 0; padding: 0; }
  html, body {
    width: 1200px; height: 1001px; overflow: hidden;
    background: var(--stage);
    font-family: "Lato", Arial, sans-serif;
  }
  .card {
    position: absolute; left: 306px; width: 588px; height: 330px; overflow: hidden;
  }
  .card--front { top: 146px; background: var(--paper); }
  .card--back { top: 525px; background: var(--green); }

  .front__header { position: absolute; left: 0; top: 0; width: 100%; height: 170px; }
  .person { position: absolute; left: 37px; top: 64px; }
  .person__name { color: var(--green); font-weight: 700; font-size: 19px; letter-spacing: 0.2px; }
  .person__title { color: var(--ink); font-size: 14px; margin-top: 4px; }

  .brand { position: absolute; display: flex; align-items: center; gap: 10px; color: var(--ink); font-weight: 700; }
  .brand__mark { background: var(--green); }
  .front__brand { right: 34px; top: 70px; font-size: 50px; line-height: 1; }
  .front__brand .brand__mark { width: 22px; height: 22px; }

  .front__info { position: absolute; left: 0; top: 170px; width: 100%; height: 129px; background: var(--grey); }
  .front__pointer { position: absolute; left: 36px; top: 0; width: 0; height: 0;
    border-left: 9px solid transparent; border-right: 9px solid transparent; border-top: 9px solid var(--paper); }
  .contacts { position: absolute; left: 37px; top: 38px; list-style: none; }
  .contacts li { display: flex; align-items: center; gap: 9px; color: var(--light-text); font-size: 14px; height: 18.5px; }
  .contacts svg { width: 13px; height: 13px; flex: none; }
  .address { position: absolute; right: 34px; top: 58px; text-align: right; color: var(--light-text); font-size: 14px; line-height: 17px; }
  .front__stripe { position: absolute; left: 0; top: 299px; width: 100%; height: 31px; background: var(--green); }

  .back__brand { left: 61px; top: 160px; font-size: 64px; line-height: 1; }
  .back__brand .brand__mark { width: 28px; height: 28px; background: var(--grey); }
  .back__stripe { position: absolute; left: 0; top: 298px; width: 100%; height: 32px; background: var(--grey-dark); }
</style>
</head>
<body>
  <section class="card card--front">
    <div class="front__header">
      <div class="person">
        <p class="person__name">OLENA DOVBUSH</p>
        <p class="person__title">General Manager</p>
      </div>
      <div class="brand front__brand">
        <span class="brand__mark"></span>
        <span class="brand__name">qorvil</span>
      </div>
    </div>
    <div class="front__info">
      <span class="front__pointer"></span>
      <ul class="contacts">
        <li>
          <svg viewBox="0 0 16 16" aria-hidden="true"><path fill="#6aab2e" d="M4 1l2.5 3.5-1.5 1.8c.8 2 2.4 3.7 4.5 4.6l1.7-1.5L15 12l-1.6 2.6C7.6 14.3 1.8 8.6 1.4 2.7z"/></svg>
          780.555.0187
        </li>
        <li>
          <svg viewBox="0 0 16 16" aria-hidden="true"><rect x="1" y="3" width="14" height="10" fill="#6aab2e"/><path d="M1 3l7 6 7-6" fill="none" stroke="#3e3f42" stroke-width="1.4"/></svg>
          hello@qorvil.example
        </li>
        <li>
          <svg viewBox="0 0 16 16" aria-hidden="true"><g fill="none" stroke="#6aab2e" stroke-width="1.3"><circle cx="8" cy="8" r="6.5"/><ellipse cx="8" cy="8" rx="2.8" ry="6.5"/><path d="M1.5 8h13M2.5 4.8h11M2.5 11.2h11"/></g></svg>
          www.qorvil.example
        </li>
      </ul>
      <p class="address">3306 Alder Ridge<br>Dr. Nashville, TN 37299</p>
    </div>
    <div class="front__stripe"></div>
  </section>

  <section class="card card--back">
    <div class="brand back__brand">
      <span class="brand__mark"></span>
      <span class="brand__name">qorvil</span>
    </div>
    <div class="back__stripe"></div>
  </section>
</body>
</html>
```